Talven Business Card

I have a business that is called "Talven Electrical Products LTD" My company deals with top of the range laptops and mobile phones that are exclusive. I need a business card that will be eye catching but not over complicated.

Target Market(s)

Adults aged 19 to 50
Upper middle class

Industry/Entity Type

Business

Requirements
Must have
• Company name/logo (file attached)
• It must have my contact information which is:

• Name: Dale Marwick

• Position: Managing Director 

• Business Address: 7 Hapton Row, London, E18 9QD

• Contact Number: 02085193604
• Mobile: 07814260537
• Email: info@talven-goods.co.uk
Nice to have
• Simple and stylish
• Eye catching

```html
<!DOCTYPE html>
<html lang="en">
<head>
<meta charset="utf-8">
<title>Talven Electrical Products – Business Card</title>
<link rel="stylesheet" href="https://fonts.googleapis.com/css2?family=Inter:wght@300;400;500&display=swap">
<style>
  :root {
    --sky: #62c4e6;
    --sky-light: #7fcbe6;
    --brand-blue: #1f6f9f;
    --navy: #263456;
    --ink: #34405e;
    --paper: #ffffff;
  }
  * { margin: 0; padding: 0; box-sizing: border-box; }
  html, body {
    width: 1200px;
    height: 687px;
    overflow: hidden;
    background: var(--paper);
  }
  .card {
    position: relative;
    width: 1200px;
    height: 687px;
    background: var(--paper);
    font-family: "Inter", "Helvetica Neue", Arial, sans-serif;
    color: var(--ink);
  }
  .brand-panel {
    position: absolute;
    left: 0;
    top: 0;
    width: 485px;
    height: 687px;
    background: linear-gradient(to bottom,
      var(--paper) 0px,
      var(--paper) 140px,
      #bfe6f4 215px,
      var(--sky) 295px,
      var(--sky) 687px);
  }
  .brand-name {
    position: absolute;
    left: 62px;
    top: 50px;
    font-size: 100px;
    font-weight: 400;
    line-height: 1;
    letter-spacing: 1px;
    color: var(--brand-blue);
  }
  .brand-tagline {
    position: absolute;
    left: 65px;
    top: 161px;
    font-size: 35px;
    font-weight: 300;
    letter-spacing: 4px;
    line-height: 1;
    color: var(--navy);
  }
  .contact {
    position: absolute;
    left: 552px;
    top: 222px;
  }
  .person-name {
    font-size: 45px;
    font-weight: 500;
    line-height: 50px;
    color: var(--sky-light);
    text-transform: uppercase;
  }
  .person-role {
    font-size: 42px;
    font-weight: 300;
    line-height: 50px;
    margin-top: 6px;
    color: var(--navy);
  }
  .address {
    font-style: normal;
    font-size: 40px;
    font-weight: 300;
    line-height: 51px;
    margin-top: 24px;
    color: var(--ink);
  }
  .channels {
    list-style: none;
    margin-top: 24px;
    font-size: 40px;
    font-weight: 300;
    line-height: 51px;
    color: var(--ink);
  }
  .channel-label {
    display: inline-block;
    width: 66px;
  }
</style>
</head>
<body>
  <div class="card">
    <div class="brand-panel">
      <div class="brand-name">TALVEN</div>
      <div class="brand-tagline">Electrical Products</div>
    </div>

    <div class="contact">
      <h1 class="person-name">Dale Marwick</h1>
      <p class="person-role">Managing Director</p>
      <address class="address">
        7 Hapton Row,<br>
        London, E18 9QD
      </address>
      <ul class="channels">
        <li><span class="channel-label">P:</span>020 8519 3604</li>
        <li><span class="channel-label">M:</span>078 1426 0537</li>
        <li><span class="channel-label">E:</span>info@talven-goods.co.uk</li>
      </ul>
    </div>
  </div>
</body>
</html>
```